Bref créative
Business cards, stationery, powerpoint template, and email signature for business consulting firm
Bellwether Advisory Group The Ground Level Method
Simple
Corwin Pike
Consultant
PO Box 7086
Austell, GA 30497
cpike@bellwethgrp.net
We will be adding new employees so I would like the business card file to be changeable. I would like to see both one sided and two-sided business cards.
The logo files will have all parts of the logo available both separate and complete.
This is the complete logo
This is the file with the logo components

```html
<!DOCTYPE html>
<html lang="en">
<head>
<meta charset="utf-8">
<title>Bellwether Advisory Group – Business Card</title>
<link rel="stylesheet" href="https://fonts.googleapis.com/css2?family=Cinzel:wght@400;600&display=swap">
<style>
  :root {
    --bg: #d9d9d9;
    --card-black: #0b0b0b;
    --card-white: #ffffff;
    --accent-green: #2e9a3a;
    --ink-dark: #1f2a22;
    --ink-light: #f2f2f2;
    --ink-muted: #8a8a8a;
    --icon-fill: #ffffff;
  }
  * { margin: 0; padding: 0; box-sizing: border-box; }
  html, body { width: 1200px; height: 895px; overflow: hidden; }
  body {
    background: var(--bg);
    font-family: "Cinzel", "Times New Roman", serif;
  }
  .card {
    position: absolute;
    left: 240px;
    width: 720px;
    height: 411px;
    overflow: hidden;
    box-shadow: 0 6px 18px rgba(0,0,0,.18);
  }
  .card--front { top: 30px; background: var(--card-white); }
  .card--back  { top: 456px; background: var(--card-black); }

  .front-shape { position: absolute; inset: 0; }

  .person {
    position: absolute;
    left: 34px;
    top: 40px;
    color: var(--ink-light);
  }
  .person__name { font-size: 24px; font-weight: 400; letter-spacing: 1px; }
  .person__title { font-size: 15px; margin-top: 4px; letter-spacing: .5px; }

  .contact-list {
    position: absolute;
    left: 34px;
    top: 200px;
    list-style: none;
    color: var(--ink-light);
    font-size: 13px;
    line-height: 1.25;
  }
  .contact-list li { display: flex; align-items: flex-start; gap: 9px; margin-bottom: 5px; }
  .contact-list svg { flex: none; width: 14px; height: 14px; margin-top: 1px; }

  .brand {
    position: absolute;
    left: 392px;
    top: 118px;
    width: 300px;
    text-align: center;
  }
  .brand__mark {
    width: 46px; height: 46px; border-radius: 50%;
    background: var(--accent-green);
    margin: 0 auto 16px;
  }
  .brand__name {
    font-size: 30px;
    font-weight: 600;
    color: var(--ink-dark);
    line-height: 1.15;
    letter-spacing: 1px;
  }
  .brand__tagline {
    font-size: 12px;
    color: var(--ink-dark);
    letter-spacing: 2px;
    margin-top: 10px;
  }

  .back-brand {
    position: absolute;
    left: 0; right: 0;
    top: 140px;
    text-align: center;
  }
  .back-brand__mark {
    width: 46px; height: 46px; border-radius: 50%;
    background: var(--accent-green);
    margin: 0 auto 16px;
  }
  .back-brand__name {
    font-size: 20px;
    font-weight: 600;
    color: var(--ink-light);
    letter-spacing: 2px;
  }
  .back-brand__web {
    margin-top: 18px;
    font-size: 11px;
    color: var(--ink-muted);
    letter-spacing: 5px;
  }
</style>
</head>
<body>

<section class="card card--front">
  <svg class="front-shape" viewBox="0 0 720 411" width="720" height="411" aria-hidden="true">
    <path d="M0 0 H285 C345 110 345 300 270 411 H0 Z" fill="var(--card-black)"/>
    <path d="M300 0 C362 110 362 300 287 411" fill="none" stroke="var(--accent-green)" stroke-width="12"/>
  </svg>

  <div class="person">
    <h1 class="person__name">Corwin Pike</h1>
    <p class="person__title">Consultant</p>
  </div>

  <ul class="contact-list">
    <li>
      <svg viewBox="0 0 14 14"><path d="M7 1a4 4 0 0 1 4 4c0 3-4 8-4 8S3 8 3 5a4 4 0 0 1 4-4z" fill="var(--icon-fill)"/><circle cx="7" cy="5" r="1.5" fill="var(--card-black)"/></svg>
      <span>PO Box 7086<br>Fernvale, OR 30497</span>
    </li>
    <li>
      <svg viewBox="0 0 14 14"><path d="M3 1h3l1 3-2 1a8 8 0 0 0 4 4l1-2 3 1v3a2 2 0 0 1-2 2A11 11 0 0 1 1 3a2 2 0 0 1 2-2z" fill="var(--icon-fill)"/></svg>
      <span>404 555 0172</span>
    </li>
    <li>
      <svg viewBox="0 0 14 14"><rect x="1" y="3" width="12" height="8" fill="var(--icon-fill)"/><path d="M1 3l6 5 6-5" fill="none" stroke="var(--card-black)" stroke-width="1"/></svg>
      <span>cpike@bellwethgrp.net</span>
    </li>
    <li>
      <svg viewBox="0 0 14 14"><circle cx="7" cy="7" r="5.5" fill="none" stroke="var(--icon-fill)" stroke-width="1.2"/><ellipse cx="7" cy="7" rx="2.3" ry="5.5" fill="none" stroke="var(--icon-fill)" stroke-width="1"/><path d="M1.5 7h11" stroke="var(--icon-fill)" stroke-width="1"/></svg>
      <span>www.bellwethgrp.net</span>
    </li>
  </ul>

  <div class="brand">
    <div class="brand__mark"></div>
    <p class="brand__name">Bellwether<br>Advisory Group</p>
    <p class="brand__tagline">The Ground Level Method</p>
  </div>
</section>

<section class="card card--back">
  <div class="back-brand">
    <div class="back-brand__mark"></div>
    <p class="back-brand__name">Bellwether Advisory Group</p>
    <p class="back-brand__web">www.bellwethgrp.net</p>
  </div>
</section>

</body>
</html>
```